IT company needs new and creative business card!

As it is very urgent, the designer who send designs first will have more chance to win.
Please send a new creative business card design with our new logo.
Please send us an 'able to edit' 'open art' as we have many employees to issue business cards (different names, positions, contacts).
The business card must show the Name of the person, position, contact the details and company information as it below:
e.g name of the person: Renato Colussi
e.g. positions Exective Director
our website www.brindlecore.com.au
e.g person's e-mail rcolussi@brindlecore.com.au
e.g. person mobile number m.+61 0400 718 354
company's address: Level 5, 14 Quarry Rd North Sydney NSW 2060

Project Deadline Extended Reason: I've just decided to update my logo (after started this project) so I am running other project to later come back here and update the brief attaching the new logo to then design the business card. Added Tuesday, February 28, 2017

Target Market(s)

IT

Industry/Entity Type

It Company

Contact Information for Business Card

The business card should show the Name of the person, position, contact the details and company information.

Requirements
Must have
• The business card must show the Name of the person, position, contact the details and company information as it below:
• e.g name of the person: Renato Colussi
• e.g. positions Exective Director
• our website www.brindlecore.com.au
• e.g person's e-mail rcolussi@brindlecore.com.au
• e.g. person mobile number m.+61 0400 718 354
• company's address: Level 5, 14 Quarry Rd North Sydney NSW 2060

```html
<!DOCTYPE html>
<html lang="en">
<head>
<meta charset="utf-8">
<title>Brindlecore business card</title>
<link rel="stylesheet" href="https://fonts.googleapis.com/css2?family=Quicksand:wght@700&family=Open+Sans:wght@400;600;700&display=swap">
<style>
  :root {
    --stage: #000000;
    --brand-blue: #0f5aa5;
    --sky-blue: #2ea4dc;
    --pale-blue: #8fd3f3;
    --paper: #f7f7f7;
    --white: #ffffff;
  }
  * { margin: 0; padding: 0; box-sizing: border-box; }
  html, body { width: 1200px; height: 1000px; overflow: hidden; background: var(--stage); }
  .canvas { position: relative; width: 1200px; height: 1000px; }
  .card {
    position: absolute; left: 299px; width: 598px; height: 369px;
    background: var(--brand-blue); overflow: hidden;
  }
  .card--front { top: 115px; }
  .card--back { top: 524px; }

  .front__name {
    position: absolute; left: 0; right: 0; top: 148px;
    text-align: center; color: var(--white);
    font-family: "Quicksand", sans-serif; font-weight: 700;
    font-size: 50px; letter-spacing: 2px; line-height: 1;
  }

  .back__panel { position: absolute; inset: 0; }

  .person {
    position: absolute; right: 38px; top: 40px; text-align: right;
    font-family: "Open Sans", sans-serif; color: var(--brand-blue);
  }
  .person__name { font-size: 20px; line-height: 1.1; letter-spacing: -0.3px; }
  .person__first { font-weight: 700; }
  .person__last { font-weight: 400; }
  .person__role { font-size: 13px; font-weight: 700; color: var(--sky-blue); margin-top: 2px; }

  .contacts {
    position: absolute; left: 38px; top: 228px; list-style: none;
    font-family: "Open Sans", sans-serif; font-weight: 600;
    font-size: 14px; color: var(--white);
  }
  .contacts li { display: flex; align-items: center; height: 19.5px; }
  .contacts svg { width: 14px; height: 14px; margin-right: 8px; flex: none; }

  .address {
    position: absolute; left: 38px; top: 299px;
    font-family: "Open Sans", sans-serif; font-weight: 600;
    font-size: 14px; line-height: 18px; color: var(--white); font-style: normal;
  }
</style>
</head>
<body>
<main class="canvas">
  <section class="card card--front" aria-label="Card front">
    <p class="front__name">BRINDLECORE</p>
  </section>

  <section class="card card--back" aria-label="Card back">
    <svg class="back__panel" viewBox="0 0 598 369" width="598" height="369" aria-hidden="true">
      <path d="M192 0 C140 40 168 150 330 250 C430 312 540 350 598 362 L598 0 Z" fill="var(--paper)"/>
      <path d="M192 0 C140 40 168 150 330 250 C430 312 540 350 598 362" fill="none" stroke="var(--pale-blue)" stroke-width="4"/>
    </svg>

    <div class="person">
      <p class="person__name"><span class="person__first">Renato</span><span class="person__last">Colussi</span></p>
      <p class="person__role">Exective Director</p>
    </div>

    <ul class="contacts">
      <li>
        <svg viewBox="0 0 14 14"><rect x="3" y="0.5" width="8" height="13" rx="1.2" fill="none" stroke="var(--white)" stroke-width="1.4"/><rect x="5.5" y="10.5" width="3" height="1.2" fill="var(--white)"/></svg>
        +61 0400 718 354
      </li>
      <li>
        <svg viewBox="0 0 14 14"><rect x="0.5" y="2.5" width="13" height="9" fill="var(--white)"/><path d="M0.5 2.5 L7 8 L13.5 2.5" fill="none" stroke="var(--brand-blue)" stroke-width="1.2"/></svg>
        rcolussi@brindlecore.com.au
      </li>
      <li>
        <svg viewBox="0 0 14 14"><circle cx="7" cy="7" r="6.3" fill="none" stroke="var(--white)" stroke-width="1.3"/><ellipse cx="7" cy="7" rx="2.6" ry="6.3" fill="none" stroke="var(--white)" stroke-width="1.1"/><path d="M1 7 H13" stroke="var(--white)" stroke-width="1.1"/></svg>
        www.brindlecore.com.au
      </li>
    </ul>

    <address class="address">Level 5, 14 Quarry Rd North<br>Sydney NSW 2060</address>
  </section>
</main>
</body>
</html>
```